pharmacy/travel clinic business card design

We need a business card for our new business called Merrow Travel Clinic and Pharmacy. Our primary focus is doing consultations for people before travelling internationally and providing vaccinations and prescriptions for them. While the business is considered a pharmacy, it has more the look and feel of a doctor's office. The design should communicate a professional and trustworthy feel. I have attached a copy of the logo we are going to be using.
Updates
Thanks for the submissions.  If you haven`t been eliminated you are one of the finalists.  Decision will likely be made tomorrow.

Target Market(s)
Customers, other health care professionals, travel agents
Industry/Entity Type
Clinic
Look and feel
Each slider illustrates characteristics of the customer's brand and the style your logo design should communicate.

```html
<!DOCTYPE html>
<html lang="en">
<head>
<meta charset="utf-8">
<title>Merrow Travel Clinic and Pharmacy – Business Card</title>
<link href="https://fonts.googleapis.com/css2?family=Montserrat:wght@600;700&family=Rubik:wght@400;500&display=swap" rel="stylesheet">
<style>
  :root {
    --page: #ecebe8;
    --white: #ffffff;
    --paper: #f4f5f6;
    --green: #7ab535;
    --blue-light: #1a7fc8;
    --blue-mid: #1f62b3;
    --blue-deep: #26399a;
    --ink-brand: #1f6fbf;
    --text-light: #ffffff;
  }
  * { box-sizing: border-box; margin: 0; padding: 0; }
  html, body {
    width: 1200px; height: 880px; overflow: hidden;
    background: var(--page);
  }
  .canvas {
    width: 1200px; height: 880px;
    display: flex; flex-direction: column;
    align-items: center; justify-content: center; gap: 56px;
  }
  .card {
    position: relative;
    width: 620px; height: 354px;
    overflow: hidden;
    box-shadow: 0 6px 18px rgba(0,0,0,.18);
    font-family: "Rubik", Arial, sans-serif;
  }

  /* Wordmark: invented name set as plain text in one colour and weight */
  .wordmark {
    position: absolute;
    display: flex; align-items: center; gap: 12px;
    font-family: "Montserrat", Arial, sans-serif;
    font-weight: 700;
    white-space: nowrap;
    line-height: 1;
  }
  .wordmark__dot {
    flex: none; width: 14px; height: 14px; border-radius: 50%;
    background: currentColor;
  }

  /* Front: contact side */
  .card--front { background: var(--paper); }
  .card--front .wordmark {
    left: 40px; top: 66px;
    font-size: 25px; color: var(--ink-brand);
  }

  .name-band {
    position: absolute; left: 0; right: 0; top: 158px; height: 40px;
    background: var(--green);
    display: flex; align-items: center;
    padding-left: 80px; gap: 14px; color: var(--text-light);
  }
  .name-band__name {
    font-family: "Montserrat", Arial, sans-serif;
    font-weight: 700; font-size: 25px;
  }
  .name-band__role { font-size: 15px; }

  .contact-panel {
    position: absolute; left: 0; right: 0; top: 198px; bottom: 0;
    background: linear-gradient(100deg, var(--blue-light) 0%, var(--blue-mid) 55%, var(--blue-deep) 100%);
    border-top: 3px solid var(--white);
    color: var(--text-light);
  }
  .contact-list {
    position: absolute; left: 40px; top: 26px;
    list-style: none; font-size: 15px; line-height: 30px;
  }
  .contact-list li, .address { display: flex; align-items: center; gap: 12px; }
  .contact-list svg, .address svg { flex: none; }
  .address {
    position: absolute; left: 350px; top: 40px;
    align-items: flex-start; font-size: 15px; line-height: 24px;
    font-style: normal;
  }
  .address svg { margin-top: 4px; }

  /* Back: brand side */
  .card--back {
    background: linear-gradient(110deg, var(--blue-light) 0%, var(--blue-mid) 50%, var(--blue-deep) 100%);
  }
  .card--back .wordmark {
    left: 50%; top: 50%; transform: translate(-50%, -50%);
    font-size: 26px; color: var(--white);
  }
</style>
</head>
<body>
<main class="canvas">

  <section class="card card--front" aria-label="Business card, contact side">
    <div class="wordmark">
      <span class="wordmark__dot" aria-hidden="true"></span>
      <span>Merrow Travel Clinic and Pharmacy</span>
    </div>

    <div class="name-band">
      <span class="name-band__name">Dr. Name Surname</span>
      <span class="name-band__role">| Something Specialist</span>
    </div>

    <div class="contact-panel">
      <ul class="contact-list">
        <li>
          <svg width="12" height="16" viewBox="0 0 12 16" aria-hidden="true"><rect x="1.5" y="1" width="9" height="14" rx="2" fill="none" stroke="#fff" stroke-width="1.6"/><circle cx="6" cy="12.3" r="1" fill="#fff"/></svg>
          (+00) 123 456 789
        </li>
        <li>
          <svg width="15" height="11" viewBox="0 0 15 11" aria-hidden="true"><rect x="0" y="0" width="15" height="11" rx="1.5" fill="#fff"/><path d="M1 1.5 L7.5 6.5 L14 1.5" fill="none" stroke="#1f62b3" stroke-width="1.4"/></svg>
          name@merrowtravelclinic.com
        </li>
        <li>
          <svg width="14" height="14" viewBox="0 0 14 14" aria-hidden="true"><g fill="none" stroke="#fff" stroke-width="1.3"><circle cx="7" cy="7" r="6"/><ellipse cx="7" cy="7" rx="2.6" ry="6"/><path d="M1 7h12"/></g></svg>
          www.merrowtravelclinic.com
        </li>
      </ul>
      <address class="address">
        <svg width="13" height="18" viewBox="0 0 13 18" aria-hidden="true"><path d="M6.5 0C2.9 0 0 2.8 0 6.4 0 11 6.5 18 6.5 18S13 11 13 6.4C13 2.8 10.1 0 6.5 0z" fill="#fff"/><circle cx="6.5" cy="6.3" r="2.4" fill="#1f62b3"/></svg>
        <span>Your Address Goes Here<br>Suite 300<br>City, Country, Zipcode</span>
      </address>
    </div>
  </section>

  <section class="card card--back" aria-label="Business card, brand side">
    <div class="wordmark">
      <span class="wordmark__dot" aria-hidden="true"></span>
      <span>Merrow Travel Clinic and Pharmacy</span>
    </div>
  </section>

</main>
</body>
</html>
```